Hip surgeon needs a stationery design

I need a new stationery design for my private practice.
My practice is focused in hip arthroplasty (hip prosthesis).
I'd like to see designs most in blue or shades of blue.
I've uploaded my new logo to help with the task.
Also, I'm a member of some societies and I've uploaded their logos either, so I'd like to see them in some of the stationeries.
Itens list:
business card
letterhead A4
envelope
prescription block A5
one fold for A4 (please see the archive "pocket")
Personal data:
Dr. Renan L. Vasconti
CRM/PR 57316
site: www.clinicapelvora.com.br
email: dr.renan@clinicapelvora.com.br
Adress:
Rua Leopoldo Marques Vieira de Lima, 712
Campo Sereno - Curitiba/PR
41 30875316 I 30875317
Updates
I forgot to mention that my practice is focused primarily in hip arthroplasty (total hip prosthesis) and the target audience range from young adults to the elderly.
I also perform hip preserving surgeries (open and arthroscopic procedures) and pelvic and hip fracture surgery (trauma).
- Any "cleaner" fonts are welcome

```html
<!DOCTYPE html>
<html lang="pt-BR">
<head>
<meta charset="utf-8">
<title>Prescription – A5 Portrait and A5 Landscape</title>
<link rel="stylesheet" href="https://fonts.googleapis.com/css2?family=Roboto:wght@400&family=Exo+2:wght@500&family=Lato:wght@400&family=Arimo:wght@400&display=swap">
<style>
  :root {
    --backdrop: #8f8f8f;
    --paper: #ffffff;
    --brand-blue: #1a8fd8;
    --ink: #2b2b2b;
    --rule-grey: #3a3a3a;
    --caption: #e9e9e9;
  }
  * { box-sizing: border-box; margin: 0; padding: 0; }
  html, body { width: 1200px; height: 640px; overflow: hidden; }
  body { background: var(--backdrop); position: relative; font-family: "Arimo", Arial, sans-serif; color: var(--ink); }

  .sheet { position: absolute; background: var(--paper); box-shadow: 2px 3px 4px rgba(0,0,0,.35); overflow: hidden; }
  .sheet--portrait { left: 40px; top: 22px; width: 419px; height: 594px; }
  .sheet--landscape { left: 502px; top: 22px; width: 640px; height: 452px; }

  .brand { position: absolute; display: flex; align-items: center; }
  .brand__mark { border-radius: 50%; background: var(--brand-blue); flex: none; }
  .brand__text { color: var(--brand-blue); font-family: "Roboto", Arial, sans-serif; font-weight: 400; line-height: 1.05; }
  .sheet--portrait .brand { left: 28px; top: 25px; gap: 6px; }
  .sheet--portrait .brand__mark { width: 44px; height: 44px; }
  .sheet--portrait .brand__name { font-size: 19px; }
  .sheet--portrait .brand__tagline { font-size: 14px; }
  .sheet--landscape .brand { left: 27px; top: 31px; gap: 7px; }
  .sheet--landscape .brand__mark { width: 54px; height: 54px; }
  .sheet--landscape .brand__name { font-size: 24px; }
  .sheet--landscape .brand__tagline { font-size: 17px; }

  .contacts { position: absolute; list-style: none; }
  .contacts li { display: flex; align-items: center; gap: 3px; white-space: nowrap; }
  .contacts svg { flex: none; }
  .sheet--portrait .contacts { left: 270px; top: 32px; font-size: 7.4px; }
  .sheet--portrait .contacts li { height: 11.2px; }
  .sheet--portrait .contacts svg { width: 9px; height: 9px; }
  .sheet--landscape .contacts { left: 470px; top: 39px; font-size: 8px; }
  .sheet--landscape .contacts li { height: 11.7px; }
  .sheet--landscape .contacts svg { width: 10px; height: 10px; }

  .header-rule { position: absolute; height: 1.5px; background: var(--brand-blue); }
  .sheet--portrait .header-rule { left: 29px; width: 365px; top: 85px; }
  .sheet--landscape .header-rule { left: 34px; width: 571px; top: 96px; }

  .field { position: absolute; display: flex; align-items: flex-end; font-size: 7.5px; }
  .field__line { border-bottom: 0.8px solid var(--rule-grey); margin-left: 4px; height: 1px; margin-bottom: 1px; }
  .sheet--landscape .field { font-size: 8.5px; }

  .signature { position: absolute; text-align: right; }
  .signature__name { font-family: "Exo 2", Arial, sans-serif; font-weight: 500; color: var(--brand-blue); letter-spacing: .3px; }
  .signature__reg { font-size: 6.8px; margin-top: 3px; }
  .sheet--portrait .signature { right: 27px; top: 540px; }
  .sheet--portrait .signature__name { font-size: 10.5px; }
  .sheet--landscape .signature { right: 38px; top: 398px; }
  .sheet--landscape .signature__name { font-size: 12px; }
  .sheet--landscape .signature__reg { font-size: 7.2px; }

  .caption { position: absolute; left: 578px; top: 530px; font-family: "Lato", Arial, sans-serif; font-size: 15.5px; line-height: 20px; color: var(--caption); }
</style>
</head>
<body>

<!-- A5 portrait prescription -->
<section class="sheet sheet--portrait">
  <div class="brand">
    <span class="brand__mark"></span>
    <div class="brand__text">
      <div class="brand__name">Dr. Renan L. Vasconti</div>
      <div class="brand__tagline">Cirurgia do Quadril</div>
    </div>
  </div>
  <ul class="contacts">
    <li><svg viewBox="0 0 10 10"><circle cx="5" cy="5" r="5" fill="#1a8fd8"/><rect x="2.6" y="3.6" width="4.8" height="3" rx=".8" fill="#fff"/></svg>41-30875316 | 30875317</li>
    <li><svg viewBox="0 0 10 10"><circle cx="5" cy="5" r="5" fill="#1a8fd8"/><rect x="2.5" y="3.2" width="5" height="3.6" fill="#fff"/></svg>dr.renan@clinicapelvora.com.br</li>
    <li><svg viewBox="0 0 10 10"><circle cx="5" cy="5" r="5" fill="#1a8fd8"/><circle cx="5" cy="5" r="2.6" fill="none" stroke="#fff" stroke-width=".9"/></svg>www.clinicapelvora.com.br</li>
    <li><svg viewBox="0 0 10 10"><circle cx="5" cy="5" r="5" fill="#1a8fd8"/><path d="M5 8.2 3 5a2 2 0 1 1 4 0z" fill="#fff"/></svg>2/114 Streetame, City, PO BOX 2222</li>
  </ul>
  <div class="header-rule"></div>

  <div class="field" style="left:28px; top:101px;">Patient Name:<span class="field__line" style="width:203px"></span></div>
  <div class="field" style="left:294px; top:101px;">Date:<span class="field__line" style="width:78px"></span></div>
  <div class="field" style="left:28px; top:123px;">Patient&nbsp; Adress:<span class="field__line" style="width:309px"></span></div>

  <div class="signature">
    <div class="signature__name">Dr. Renan L. Vasconti</div>
    <div class="signature__reg">CRM/PR 57316</div>
  </div>
</section>

<!-- A5 landscape prescription -->
<section class="sheet sheet--landscape">
  <div class="brand">
    <span class="brand__mark"></span>
    <div class="brand__text">
      <div class="brand__name">Dr. Renan L. Vasconti</div>
      <div class="brand__tagline">Cirurgia do Quadril</div>
    </div>
  </div>
  <ul class="contacts">
    <li><svg viewBox="0 0 10 10"><circle cx="5" cy="5" r="5" fill="#1a8fd8"/><rect x="2.6" y="3.6" width="4.8" height="3" rx=".8" fill="#fff"/></svg>41-30875316 | 30875317</li>
    <li><svg viewBox="0 0 10 10"><circle cx="5" cy="5" r="5" fill="#1a8fd8"/><rect x="2.5" y="3.2" width="5" height="3.6" fill="#fff"/></svg>dr.renan@clinicapelvora.com.br</li>
    <li><svg viewBox="0 0 10 10"><circle cx="5" cy="5" r="5" fill="#1a8fd8"/><circle cx="5" cy="5" r="2.6" fill="none" stroke="#fff" stroke-width=".9"/></svg>www.clinicapelvora.com.br</li>
    <li><svg viewBox="0 0 10 10"><circle cx="5" cy="5" r="5" fill="#1a8fd8"/><path d="M5 8.2 3 5a2 2 0 1 1 4 0z" fill="#fff"/></svg>2/114 Streetame, City, PO BOX 2222</li>
  </ul>
  <div class="header-rule"></div>

  <div class="field" style="left:48px; top:113px;">Patient Name:<span class="field__line" style="width:301px"></span></div>
  <div class="field" style="left:420px; top:113px;">Date:<span class="field__line" style="width:161px"></span></div>
  <div class="field" style="left:48px; top:137px;">Patient&nbsp; Adress:<span class="field__line" style="width:500px"></span></div>

  <div class="signature">
    <div class="signature__name">Dr. Renan L. Vasconti</div>
    <div class="signature__reg">CRM/PR 57316</div>
  </div>
</section>

<div class="caption">Prescription<br>A5_Portrait<br>A5 Landscape</div>

</body>
</html>
```